Mortgage Loan officer needs clean/modern business card design

Looking for a clean, modern 2-sided business card design. We like the earth tones used in our logo and website http://varnhill-lending.com . Would also like to incorporate: 1) Something special to make our card stand out - a pop of color or embossed logo, for instance and 2) please include "Mortgage Loans" "Reverse Mortgages" "Private Money Loans" on back of card with the logo.

Front: Needs to include agent/company license info - see website. Agent name: Marco Lindqvist

Here are fonts and colors used for our logo:
Font: Avenir Next
Colors:
#2c3539 - Dark Gray
#576870 - Light Gray
#ffffff - Background White

Target Market(s)

Prospects and current clients. Will also be distributing to people in professional network (attorneys and CPAs)

Industry/Entity Type

Business

Contact Information for Business Card

Include agent name, contact info, website on front, licensing info for agent an company. Logo and services offered on back

Font styles to use
Other font styles liked:
• Avenir Next

Requirements
Must have
• See project description
Should not have
• Nothing cheesy

```html
<!DOCTYPE html>
<html lang="en">
<head>
<meta charset="utf-8">
<title>Varnhill Lending – Business Card</title>
<link href="https://fonts.googleapis.com/css2?family=Nunito+Sans:ital,wght@0,400;0,600;1,400&display=swap" rel="stylesheet">
<style>
  :root {
    --dark-gray: #2c3539;
    --light-gray: #576870;
    --card-back: #4b5a62;
    --paper: #f3f4f5;
    --white: #ffffff;
    --page: #d9dcde;
    --text: #2f3336;
  }
  * { margin: 0; padding: 0; box-sizing: border-box; }
  html, body { width: 1105px; height: 1200px; overflow: hidden; }
  body {
    background: var(--page);
    font-family: "Nunito Sans", "Avenir Next", sans-serif;
    color: var(--text);
    position: relative;
  }
  .card {
    position: absolute;
    left: 182px;
    width: 747px;
    height: 426px;
    overflow: hidden;
  }
  .card-front { top: 119px; background: var(--paper); }
  .card-back { top: 638px; background: var(--card-back); }

  /* Front */
  .brand-seal {
    position: absolute;
    left: 522px; top: 8px;
    width: 188px; height: 188px;
    border: 1.5px solid var(--light-gray);
    border-radius: 50%;
    display: flex; align-items: center; justify-content: center;
    text-align: center;
  }
  .brand-seal .brand-name {
    font-size: 24px; font-weight: 600; line-height: 1.15;
    color: var(--dark-gray);
  }
  .agent-name {
    position: absolute; left: 43px; top: 176px;
    font-size: 26px; font-weight: 600; letter-spacing: 0.5px;
    color: var(--dark-gray);
  }
  .agent-title {
    position: absolute; left: 43px; top: 208px;
    font-size: 19px; color: var(--light-gray);
  }
  .divider {
    position: absolute; left: 43px; top: 244px;
    width: 666px; height: 1.5px; background: var(--dark-gray);
  }
  .contact-list { position: absolute; left: 46px; top: 257px; list-style: none; }
  .contact-list li {
    display: flex; align-items: center; gap: 10px;
    height: 29px; font-size: 19px; color: var(--text);
  }
  .contact-list svg { width: 17px; height: 17px; fill: var(--dark-gray); }
  .office {
    position: absolute; right: 37px; top: 278px;
    text-align: right; font-size: 19px; line-height: 28px;
  }
  .office .license { margin-top: 6px; }
  .footer-band { position: absolute; left: 0; bottom: 0; width: 747px; height: 48px; }
  .footer-url {
    position: absolute; right: 38px; bottom: 14px;
    font-size: 19px; font-style: italic; letter-spacing: 1.6px;
    color: var(--white);
  }

  /* Back */
  .back-surface { position: absolute; inset: 0; background: var(--card-back); }
  .back-brand {
    position: absolute; left: 0; right: 0; top: 120px;
    text-align: center;
    font-size: 72px; font-weight: 400; line-height: 1.05;
    color: var(--paper);
  }
  .services {
    position: absolute; left: 0; right: 0; top: 368px;
    text-align: center; font-size: 20px; color: #e6e9ea;
  }
</style>
</head>
<body>

<section class="card card-front" aria-label="Card front">
  <div class="brand-seal"><span class="brand-name">Varnhill<br>Lending</span></div>

  <h1 class="agent-name">MARCO LINDQVIST</h1>
  <p class="agent-title">CEO/Founder</p>
  <div class="divider"></div>

  <ul class="contact-list">
    <li><svg viewBox="0 0 24 24"><path d="M6.6 10.8a15 15 0 0 0 6.6 6.6l2.2-2.2c.3-.3.7-.4 1-.2 1.1.4 2.3.6 3.6.6.6 0 1 .4 1 1V20c0 .6-.4 1-1 1C10.6 21 3 13.4 3 4c0-.6.4-1 1-1h3.5c.6 0 1 .4 1 1 0 1.3.2 2.5.6 3.6.1.3 0 .7-.2 1z"/></svg>408-555-0140 x212</li>
    <li><svg viewBox="0 0 24 24"><path d="M6.6 10.8a15 15 0 0 0 6.6 6.6l2.2-2.2c.3-.3.7-.4 1-.2 1.1.4 2.3.6 3.6.6.6 0 1 .4 1 1V20c0 .6-.4 1-1 1C10.6 21 3 13.4 3 4c0-.6.4-1 1-1h3.5c.6 0 1 .4 1 1 0 1.3.2 2.5.6 3.6.1.3 0 .7-.2 1z"/></svg>650-555-0187</li>
    <li><svg viewBox="0 0 24 24"><path d="M6 3h10l2 2v4H6z"/><path d="M2 10h20v8h-3v-3H5v3H2z"/><path d="M6 16h12v5H6z"/></svg>408-555-0163</li>
    <li><svg viewBox="0 0 24 24"><path d="M2 5h20v14H2z" fill="none" stroke="#2c3539" stroke-width="2"/><path d="M2 5l10 8 10-8" fill="none" stroke="#2c3539" stroke-width="2"/></svg>varnhill-lending.com</li>
  </ul>

  <address class="office" style="font-style:normal">
    <div>2480 Harlow Avenue, Suite 310</div>
    <div>Cedar Bay, CA 95014</div>
    <div class="license">Lic No :NMLS:501246</div>
  </address>

  <svg class="footer-band" viewBox="0 0 747 48" preserveAspectRatio="none" aria-hidden="true">
    <path d="M0 18 H385 Q398 18 404 26 L406 28 H0 Z" fill="var(--dark-gray)"/>
    <path d="M420 0 H747 V35 H400 Q408 5 430 0 Z" fill="var(--light-gray)"/>
    <rect x="0" y="35" width="747" height="13" fill="var(--paper)"/>
  </svg>
  <span class="footer-url">www.varnhill-lending.com</span>
</section>

<section class="card card-back" aria-label="Card back">
  <div class="back-surface" role="img" aria-label="Subtle overlapping circle pattern in slate gray tones"></div>
  <div class="back-brand">Varnhill<br>Lending</div>
  <p class="services">Mortgage Loans • Reverse Mortgages • Private Money Loans</p>
</section>

</body>
</html>
```